Pitch book for Birchmere Property Partners.

Birchmere Partners is a new real estate investment company focused on multifamily (apartment) investments along the San Francisco Peninsula (in other parts of the world it is also referred to as flats). We need a professional Pitch Book i.e. brochure (digital and print) to raise equity from private investors. Read about “pitch book” on Lexipedia. The profile of the investor is conservative and must qualify as an accredited investor. Think high net worth individuals, CEOs and wealthy retiring couples. The investor that is attracted to real estate invest because it is low risk, produce cash flow and provide solid returns over the long term.

The brochure should convey trust, be highly professional and be clean and crisp. I attach a PowerPoint doc to be used as a copy for the brochure. I also attach a brochure of Halvert Crane – I like the look and feel, think it was designed with InDesign.

We will use the brochure at one-on-one meetings with investors where we will present on a laptop; we also need it in a format so that we can email it, print it and use it to be uploaded as a website.

I prefer the up and down scroll format (like you would do on a Mac) compared to PowerPoint but I am open to suggestions.

The photos I used in the PowerPoint presentation was found on the web, please use your own stock images.

Target Market(s)

High net worth individuals

Industry/Entity Type

Real Estate

Font styles to use
Serif

Requirements
Must have
• See attached Power Point
Nice to have
• See attached HVC brochure, I like the look and feel.
Should not have
• I am open to your ideas.

```html
<!DOCTYPE html>
<html lang="en">
<head>
<meta charset="utf-8">
<title>Birchmere Property Partners – Pitch Book Spreads</title>
<link href="https://fonts.googleapis.com/css2?family=Tinos:ital,wght@0,400;1,400&display=swap" rel="stylesheet">
<style>
  :root{
    --backdrop:#d3d3d3;
    --paper:#ffffff;
    --ink:#2b2b2b;
    --ink-soft:#4a4a4a;
    --muted:#9a9a9a;
    --rule:#b9b9b9;
    --white:#ffffff;
    --shadow:0 2px 5px rgba(0,0,0,.28);
  }
  *{margin:0;padding:0;box-sizing:border-box;}
  html,body{width:1200px;height:900px;overflow:hidden;background:var(--backdrop);}
  body{position:relative;font-family:"Tinos","Times New Roman",serif;color:var(--ink);}

  .page{position:absolute;width:550px;height:428px;background:var(--paper);box-shadow:var(--shadow);overflow:hidden;}
  .page--cover{left:39px;top:13px;}
  .page--opportunity{left:611px;top:13px;}
  .page--mission{left:39px;top:458px;}
  .page--lifecycle{left:611px;top:458px;}

  .photo{position:absolute;top:0;height:100%;}
  .wordmark{position:absolute;color:var(--white);font-size:13px;letter-spacing:.5px;text-align:center;}

  /* Cover */
  .cover-photo{left:0;width:100%;
    background:linear-gradient(180deg,#3e3254 0%,#5a4668 45%,#7b5a72 70%,#4a3a58 100%);}
  .cover-title{position:absolute;left:0;width:100%;top:194px;text-align:center;color:var(--white);
    font-size:33px;letter-spacing:.3px;}
  .cover-rule{position:absolute;left:205px;width:140px;top:242px;border-top:1px solid rgba(255,255,255,.8);}
  .cover-sub{position:absolute;left:0;width:100%;top:256px;text-align:center;color:var(--white);
    font-style:italic;font-size:24px;line-height:25px;}
  .page--cover .wordmark{left:0;width:100%;top:130px;font-size:15px;}

  /* Split text panels */
  .panel{position:absolute;top:0;height:100%;text-align:center;}
  .heading{font-size:17px;letter-spacing:2.6px;line-height:25px;color:var(--ink);}
  .tagline{font-size:9.5px;letter-spacing:1.2px;color:var(--muted);line-height:12px;}
  .rule{width:117px;margin:0 auto;border-top:1px solid var(--rule);}
  .body{font-size:8.6px;line-height:11.6px;color:var(--ink-soft);}
  .subhead{font-style:italic;font-size:17px;line-height:18px;color:var(--ink);}
  .note{font-size:7.8px;line-height:10.6px;color:var(--muted);}

  /* Opportunity */
  .opp-photo{left:0;width:312px;background:linear-gradient(160deg,#9a928e 0%,#6f6864 50%,#4d4744 100%);}
  .page--opportunity .wordmark{left:0;width:104px;top:388px;}
  .opp-panel{left:312px;width:238px;padding:38px 20px 0;}
  .opp-panel .tagline{margin-top:4px;}
  .opp-panel .rule:first-of-type{margin-top:18px;}
  .opp-panel .body{margin-top:20px;}
  .opp-panel .rule.second{margin-top:14px;}
  .opp-panel .subhead{margin-top:18px;}
  .reasons{list-style:none;margin-top:12px;padding:0 4px;}
  .reasons li{position:relative;font-size:8.3px;line-height:12px;color:var(--muted);margin-bottom:12px;padding-left:12px;}
  .reasons li::before{content:"•";position:absolute;left:0;top:0;}

  /* Mission */
  .mission-panel{left:0;width:313px;padding:38px 34px 0;}
  .mission-panel .tagline{margin-top:6px;}
  .pillars{margin-top:7px;font-size:9.5px;letter-spacing:1.6px;color:var(--ink);}
  .mission-panel .rule.top{margin-top:9px;}
  .mission-panel .body.goal{margin-top:12px;font-size:7.8px;line-height:10.4px;}
  .mission-panel .rule.mid{margin-top:10px;}
  .mission-panel .subhead{margin-top:13px;font-size:16.5px;}
  .mission-panel .note.intro{margin-top:11px;}
  .only-head{margin-top:6px;font-size:10.5px;color:var(--ink);}
  .criteria{list-style:none;}
  .criteria li{font-size:7.6px;line-height:10.4px;color:var(--muted);margin-top:6px;}
  .mission-photo{left:313px;width:237px;
    background:linear-gradient(180deg,#5f5a78 0%,#a07d86 22%,#8d7f8e 42%,#5c5d6f 70%,#3b3c4c 100%);}
  .page--mission .wordmark{left:313px;width:237px;top:388px;}

  /* Lifecycle */
  .life-panel{left:0;width:313px;padding:43px 0 0;}
  .steps{list-style:none;margin-top:26px;}
  .steps li{font-size:13px;letter-spacing:1.4px;line-height:15px;color:var(--ink-soft);height:32.6px;}
  .tick{display:block;margin:0 auto 2px;width:10px;height:8px;}
  .life-photo{left:313px;width:237px;background:linear-gradient(180deg,#f0eef0 0%,#dcd8dc 55%,#c9c4c9 100%);}
  .page--lifecycle .wordmark{left:313px;width:237px;top:388px;}
</style>
</head>
<body>

<section class="page page--cover">
  <div class="photo cover-photo" role="img" aria-label="Night view of the bay bridge and lit city skyline over water, tinted purple"></div>
  <div class="wordmark">BIRCHMERE</div>
  <h1 class="cover-title">SAN FRANCISCO PENINSULA</h1>
  <div class="cover-rule"></div>
  <p class="cover-sub">Multifamily Real Estate<br>Investment</p>
</section>

<section class="page page--opportunity">
  <div class="photo opp-photo" role="img" aria-label="Sepia photograph of a historic ornate apartment building on a street corner"></div>
  <div class="wordmark">BIRCHMERE</div>
  <div class="panel opp-panel">
    <h2 class="heading">YOUR<br>OPPORTUNITY</h2>
    <p class="tagline">....safety, cash flow and<br>appreciation</p>
    <div class="rule"></div>
    <p class="body">Birchmere Partners is pleased to offer you<br>the opportunity to invest in the<br>San Francisco Peninsula multifamily real<br>estate market.</p>
    <div class="rule second"></div>
    <h3 class="subhead">Why invest<br>and why here?</h3>
    <ul class="reasons">
      <li>Investing in real estate is recognized as a significant wealth-creation strategy.</li>
      <li>The San Francisco Peninsula is one of the top real estate markets in the world.</li>
      <li>The multifamily asset class is considered a low risk investment.</li>
    </ul>
  </div>
</section>

<section class="page page--mission">
  <div class="panel mission-panel">
    <h2 class="heading">OUR MISSION</h2>
    <p class="tagline">....to protect and grow your investment</p>
    <p class="pillars">FIND, BUY, HOLD FOR THE LONG-TERM</p>
    <div class="rule top"></div>
    <p class="body goal">Birchmere Partners’ core goal is to identify investments that produce consistent cash flow, have long-term value prospects not currently recognized by the market, and once acquired, increase their operational and managerial efficiencies to maximize cash flow and capital appreciation.</p>
    <div class="rule mid"></div>
    <h3 class="subhead">Why focus on a specific asset<br>class and geography?</h3>
    <p class="note intro">A focused approach is one of our competitive advantages. With 20 years real estate investment and development experience, Birchmere Partners is a Silicon Valley-based multifamily investment and advisory firm, laser-focused on growing cash flow and lasting value for our clients.</p>
    <p class="only-head">We invest only:</p>
    <ul class="criteria">
      <li>In existing properties - we can evaluate existing expenses and rent rolls with more certainty;</li>
      <li>In select San Francisco and Silicon Valley locations - we know the streets and neighborhoods;</li>
      <li>Using low risk core and core plus investment strategies - to reasonably predict cash flow; and</li>
      <li>For the long-term - your investment is a safe-haven that endures market fluctuations.</li>
    </ul>
  </div>
  <div class="photo mission-photo" role="img" aria-label="Dusk view of a pyramid skyscraper above the city with the bay and hills behind"></div>
  <div class="wordmark">BIRCHMERE</div>
</section>

<section class="page page--lifecycle">
  <div class="panel life-panel">
    <h2 class="heading">INVESTMENT<br>LIFECYCLE</h2>
    <ol class="steps">
      <li><svg class="tick" viewBox="0 0 10 8"><path d="M1 4.2 3.7 6.8 9 1" fill="none" stroke="#555" stroke-width="0.9"/></svg>Investor frmation</li>
      <li><svg class="tick" viewBox="0 0 10 8"><path d="M1 4.2 3.7 6.8 9 1" fill="none" stroke="#555" stroke-width="0.9"/></svg>Acquire asset</li>
      <li><svg class="tick" viewBox="0 0 10 8"><path d="M1 4.2 3.7 6.8 9 1" fill="none" stroke="#555" stroke-width="0.9"/></svg>Reposition</li>
      <li><svg class="tick" viewBox="0 0 10 8"><path d="M1 4.2 3.7 6.8 9 1" fill="none" stroke="#555" stroke-width="0.9"/></svg>Increase rents</li>
      <li><svg class="tick" viewBox="0 0 10 8"><path d="M1 4.2 3.7 6.8 9 1" fill="none" stroke="#555" stroke-width="0.9"/></svg>Distribute cash flow</li>
      <li><svg class="tick" viewBox="0 0 10 8"><path d="M1 4.2 3.7 6.8 9 1" fill="none" stroke="#555" stroke-width="0.9"/></svg>Asset appreciation</li>
      <li><svg class="tick" viewBox="0 0 10 8"><path d="M1 4.2 3.7 6.8 9 1" fill="none" stroke="#555" stroke-width="0.9"/></svg>Re-finance or sell asset</li>
      <li><svg class="tick" viewBox="0 0 10 8"><path d="M1 4.2 3.7 6.8 9 1" fill="none" stroke="#555" stroke-width="0.9"/></svg>Distribute profits</li>
    </ol>
  </div>
  <div class="photo life-photo" role="img" aria-label="Hand holding a pen over printed blue bar and area growth charts"></div>
  <div class="wordmark">BIRCHMERE</div>
</section>

</body>
</html>
```